Modern Infografic: redo an existing grafic

English: A detailed description of the project can be found in the appendix as PDF. In a nutshell: we have a graphical comparison, which looks old-fashioned and which we would like to have a new look. English: A detailed description of the project is attached as a pdf. In short: we have a graphic comparison, that looks old fashion and we would like to have it made new. Files: Grafic today - is the way the graphic looks today Project description EN Project description Meaning of the graphic elements description of pictures

Industry/Entity Type

It Company

Font styles to use
Sans Serif

Requirements
Must have
• The same as in the current version. But the way you show it should be modern

```html
<!DOCTYPE html>
<html lang="de">
<head>
<meta charset="utf-8">
<title>Corporate Network MPLS Deutschland – China</title>
<link rel="stylesheet" href="https://fonts.googleapis.com/css2?family=Open+Sans:wght@400;600;700&display=swap">
<style>
  :root {
    --bg: #f1f1f1;
    --ink: #1b1b1b;
    --brand-blue: #16628f;
    --title-blue: #2a7cc0;
    --line-blue: #2ea6e0;
    --router-top: #3d9fd3;
    --router-side: #1b5f88;
    --node-pink: #efc4c6;
    --node-ring: #c9c9c9;
    --node-yellow: #fbe9a6;
    --cloud: #a9d8f5;
    --cloud-text: #155e8c;
    --shield-blue: #2b78b8;
    --shield-red: #e23a3a;
    --arc: #dcdcdc;
  }
  html, body { margin: 0; padding: 0; overflow: hidden; background: var(--bg); }
  .canvas {
    position: relative; width: 1200px; height: 586px; overflow: hidden;
    background: var(--bg); font-family: "Open Sans", Arial, sans-serif; color: var(--ink);
  }
  .scene { position: absolute; inset: 0; width: 1200px; height: 586px; }
  .label { position: absolute; margin: 0; font-size: 22px; line-height: 28px; white-space: nowrap; }
  .label--center { transform: translateX(-50%); text-align: center; }
  .legend {
    position: absolute; left: 726px; top: 8px; width: 460px; height: 82px;
    background: var(--brand-blue); display: flex; align-items: center; box-sizing: border-box;
    padding-left: 10px; border: 2px solid #0f4d72;
  }
  .legend__icon { width: 72px; height: 62px; flex: none; }
  .legend__text { color: #fff; font-size: 21px; line-height: 28px; margin: 0 0 0 18px; }
  .site-title {
    position: absolute; margin: 0; color: var(--title-blue); font-weight: 700;
    font-size: 28px; line-height: 38px; letter-spacing: 0.5px;
  }
  .site-title--de { left: 18px; top: 498px; }
  .site-title--cn { right: 14px; top: 498px; text-align: right; }
  .cloud-label { position: absolute; left: 560px; top: 440px; transform: translateX(-50%);
    font-size: 44px; line-height: 52px; font-weight: 700; color: var(--cloud-text); margin: 0; }
</style>
</head>
<body>
<main class="canvas">
  <svg class="scene" viewBox="0 0 1500 733">
    <defs>
      <linearGradient id="globe-fill" x1="0" y1="0" x2="1" y2="1">
        <stop offset="0" stop-color="#7fd0f5"/><stop offset="1" stop-color="#0f5fa3"/>
      </linearGradient>
      <linearGradient id="de-fill" x1="0" y1="0" x2="0" y2="1">
        <stop offset="0" stop-color="#262626"/><stop offset="0.45" stop-color="#c0222f"/><stop offset="1" stop-color="#f8d51d"/>
      </linearGradient>
      <linearGradient id="cn-fill" x1="0" y1="0" x2="1" y2="1">
        <stop offset="0" stop-color="#d42323"/><stop offset="1" stop-color="#b51515"/>
      </linearGradient>

      <symbol id="icon-laptop" viewBox="0 0 100 80">
        <rect x="15" y="0" width="70" height="52" rx="3" fill="#333"/>
        <rect x="19" y="4" width="62" height="44" fill="currentColor"/>
        <polygon points="6,54 94,54 100,72 0,72" fill="#c8cdd2"/>
        <rect x="20" y="58" width="60" height="8" fill="#555"/>
      </symbol>
      <symbol id="icon-printer" viewBox="0 0 60 50">
        <rect x="10" y="0" width="40" height="18" rx="2" fill="#7a7a7a"/>
        <rect x="0" y="15" width="60" height="26" rx="4" fill="#4b4b4b"/>
        <polygon points="12,36 48,36 55,50 5,50" fill="#fff"/>
      </symbol>
      <symbol id="icon-phone" viewBox="0 0 30 22">
        <rect width="30" height="22" rx="4" fill="#222"/>
        <rect x="4" y="3" width="22" height="16" rx="2" fill="currentColor"/>
      </symbol>
      <symbol id="icon-tablet" viewBox="0 0 60 38">
        <rect width="60" height="38" rx="5" fill="#222"/>
        <rect x="5" y="4" width="50" height="30" rx="2" fill="currentColor"/>
      </symbol>
      <symbol id="icon-server" viewBox="0 0 44 68">
        <rect width="44" height="68" rx="3" fill="#2a3b44"/>
        <path d="M5 11 H39 M5 23 H39 M5 35 H39 M5 47 H39 M5 59 H39" stroke="#4fb3b0" stroke-width="3"/>
      </symbol>
      <symbol id="icon-router" viewBox="0 0 56 32">
        <path d="M38 14 L42 0 M46 14 L50 2" stroke="#333" stroke-width="3"/>
        <rect x="0" y="12" width="56" height="20" rx="4" fill="#4a5058"/>
        <circle cx="12" cy="22" r="2.5" fill="#7fe07f"/><circle cx="20" cy="22" r="2.5" fill="#7fe07f"/>
      </symbol>
    </defs>

    <g class="backdrop-arcs" fill="none" stroke="var(--arc)" stroke-width="7">
      <circle cx="718" cy="360" r="330"/>
      <circle cx="718" cy="360" r="560"/>
      <ellipse cx="718" cy="360" rx="760" ry="250"/>
    </g>

    <rect class="region region--de" x="50" y="345" width="470" height="295" rx="40" fill="url(#de-fill)" role="img" aria-label="Karte Deutschland in Landesfarben"/>
    <rect class="region region--cn" x="830" y="395" width="610" height="250" rx="50" fill="url(#cn-fill)" role="img" aria-label="Karte China in Landesfarben"/>

    <g class="links" stroke="var(--line-blue)" stroke-width="4" fill="none">
      <path d="M470 378 L620 560 M482 372 L632 554 M494 366 L644 548"/>
      <path d="M470 390 L400 428 M478 398 L404 436 M486 406 L408 444"/>
      <path d="M920 350 L760 530 M932 356 L772 536 M944 362 L784 542"/>
      <path d="M965 345 L1070 425 M970 335 L1075 415 M975 325 L1080 405"/>
    </g>

    <g class="lan lan--de" stroke="#fff" stroke-width="3">
      <path d="M290 470 L165 445 M290 470 L165 520 M290 470 L280 565 M290 470 L415 520 M290 470 L375 430"/>
      <circle cx="290" cy="470" r="72" fill="var(--node-pink)"/>
      <circle cx="165" cy="445" r="42" fill="var(--node-pink)"/>
      <circle cx="165" cy="520" r="38" fill="var(--node-pink)"/>
      <circle cx="280" cy="565" r="42" fill="var(--node-yellow)" stroke="var(--node-ring)"/>
      <circle cx="415" cy="520" r="45" fill="var(--node-yellow)" stroke="var(--node-ring)"/>
      <circle cx="375" cy="430" r="38" fill="var(--node-pink)"/>
    </g>
    <g class="lan-devices lan-devices--de">
      <use href="#icon-laptop" x="240" y="425" width="100" height="80" color="#fde29b" role="img" aria-label="Laptop"/>
      <use href="#icon-printer" x="137" y="420" width="56" height="48" role="img" aria-label="Drucker"/>
      <use href="#icon-phone" x="150" y="509" width="30" height="22" color="#f2e23a" role="img" aria-label="Smartphone"/>
      <use href="#icon-tablet" x="250" y="547" width="60" height="38" color="#2cc4b8" role="img" aria-label="Tablet"/>
      <use href="#icon-server" x="393" y="486" width="44" height="68" role="img" aria-label="Server"/>
      <use href="#icon-router" x="347" y="414" width="56" height="32" role="img" aria-label="Router"/>
    </g>

    <g class="lan lan--cn" stroke="#fff" stroke-width="3">
      <path d="M1160 470 L1085 435 M1160 470 L1045 525 M1160 470 L1165 565 M1160 470 L1290 520 M1160 470 L1285 440"/>
      <circle cx="1160" cy="470" r="72" fill="var(--node-pink)"/>
      <circle cx="1085" cy="435" r="38" fill="var(--node-pink)"/>
      <circle cx="1045" cy="525" r="48" fill="var(--node-pink)"/>
      <circle cx="1165" cy="565" r="42" fill="var(--node-pink)"/>
      <circle cx="1290" cy="520" r="38" fill="var(--node-pink)"/>
      <circle cx="1285" cy="440" r="42" fill="var(--node-pink)"/>
    </g>
    <g class="lan-devices lan-devices--cn">
      <use href="#icon-laptop" x="1130" y="415" width="100" height="80" color="#a5f07e" role="img" aria-label="Laptop"/>
      <use href="#icon-router" x="1057" y="418" width="56" height="32" role="img" aria-label="Router"/>
      <use href="#icon-server" x="1023" y="491" width="44" height="68" role="img" aria-label="Server"/>
      <use href="#icon-tablet" x="1135" y="547" width="60" height="38" color="#fbdc8e" role="img" aria-label="Tablet"/>
      <use href="#icon-phone" x="1275" y="509" width="30" height="22" color="#2cc4b8" role="img" aria-label="Smartphone"/>
      <use href="#icon-printer" x="1257" y="416" width="56" height="48" role="img" aria-label="Drucker"/>
    </g>

    <circle class="globe" cx="718" cy="178" r="85" fill="url(#globe-fill)" role="img" aria-label="Weltkugel Internet"/>

    <g class="firewall firewall--de">
      <path d="M530 235 Q580 215 630 240 L620 300 Q600 340 575 355 Q545 330 535 295 Z" fill="var(--shield-blue)"/>
      <path d="M545 250 Q580 236 615 252 L607 298 Q592 326 575 338 Q556 320 548 294 Z" fill="#e6eef5"/>
      <path d="M580 242 V338 M548 290 H612" stroke="var(--shield-blue)" stroke-width="4"/>
    </g>
    <g class="firewall firewall--cn">
      <path d="M790 260 Q840 225 890 230 L885 295 Q870 340 825 360 Q795 330 792 290 Z" fill="var(--shield-red)"/>
      <path d="M805 268 Q840 245 875 245 L871 293 Q860 325 827 342 Q808 320 806 290 Z" fill="#f2e4e4"/>
      <path d="M840 250 V340 M808 292 H872" stroke="var(--shield-red)" stroke-width="4"/>
    </g>

    <g class="router router--de">
      <ellipse cx="480" cy="385" rx="45" ry="18" fill="var(--router-side)"/>
      <rect x="435" y="368" width="90" height="17" fill="var(--router-side)"/>
      <ellipse cx="480" cy="368" rx="45" ry="18" fill="var(--router-top)"/>
      <path d="M462 362 L498 374 M498 362 L462 374" stroke="#fff" stroke-width="4"/>
    </g>
    <g class="router router--cn">
      <ellipse cx="945" cy="355" rx="45" ry="18" fill="var(--router-side)"/>
      <rect x="900" y="338" width="90" height="17" fill="var(--router-side)"/>
      <ellipse cx="945" cy="338" rx="45" ry="18" fill="var(--router-top)"/>
      <path d="M927 332 L963 344 M963 332 L927 344" stroke="#fff" stroke-width="4"/>
    </g>

    <path class="cloud" d="M615 620 Q590 620 592 595 Q594 570 625 570 Q625 530 665 525 Q690 490 735 505 Q775 500 785 540 Q815 545 812 580 Q812 620 780 620 Z"
      fill="var(--cloud)" stroke="#7fbfe6" stroke-width="3"/>
  </svg>

  <aside class="legend">
    <svg class="legend__icon" viewBox="0 0 72 62">
      <rect width="72" height="62" fill="#fff"/>
      <path d="M10 0 L58 62 M24 0 L72 62 M38 0 L72 44" stroke="var(--line-blue)" stroke-width="5"/>
    </svg>
    <p class="legend__text">Corporate Network Symmetrische<br>Bandbreute inkl. Router</p>
  </aside>

  <p class="label label--center" style="left:566px;top:42px;">INTERNET</p>
  <p class="label label--center" style="left:398px;top:152px;">Firewall</p>
  <p class="label" style="left:693px;top:116px;line-height:31px;">Statliche<br>Chinesische Firewall</p>
  <p class="label label--center" style="left:326px;top:216px;line-height:31px;">MPLS<br>Router</p>
  <p class="label label--center" style="left:830px;top:210px;line-height:31px;">MPLS<br>Router</p>
  <p class="label label--center" style="left:114px;top:252px;">Kunden LAN</p>
  <p class="label label--center" style="left:914px;top:286px;">Kunden LAN</p>
  <p class="cloud-label">MPLS</p>
  <p class="label label--center" style="left:578px;top:514px;line-height:30px;">Knotenpunkt in Frankfurt<br>Rechenzentrum VPN Deutschland</p>

  <h2 class="site-title site-title--de">STANDORT<br>DEUTSCHLAND</h2>
  <h2 class="site-title site-title--cn">STANDORT<br>CHINA</h2>
</main>
</body>
</html>
```